QPM Habitat Helpers 2019

We need a 2 page flyer to advertise our upcoming program. The program covers 5 months May-September 2019 and is focused on conservation.I have attached some options that i like. It needs to be striking.

Text in newly uploaded document 'HHFlyer2'

Target Market(s)

Conservation
Conscious travelers
30-45 year olds
Environmental
Adventure/Hiking
Citizen Science

Font styles to use
Sans Serif

Colors
0355a3
fbed22

Requirements
Must have
• A travel conservation focus
• Highlight the significance of the 'in the world' status of the project
Nice to have
• A yellow border, making it look similar to the cover of Wandering Horizons

```html
<!DOCTYPE html>
<html lang="en">
<head>
<meta charset="utf-8">
<title>QPM Habitat Helpers 2019 – Two Page Flyer</title>
<link rel="stylesheet" href="https://fonts.googleapis.com/css2?family=Oswald:wght@300;400;500;600&family=Roboto:wght@400;700;900&family=Dancing+Script:wght@500&display=swap">
<style>
  :root{
    --brand-blue:#0355a3;
    --brand-yellow:#fbed22;
    --backdrop:#212121;
    --white:#ffffff;
  }
  *{box-sizing:border-box;margin:0;padding:0}
  html,body{width:1200px;height:1200px;overflow:hidden;background:var(--backdrop)}
  .canvas{position:relative;width:1200px;height:1200px}
  .page{position:absolute;top:208px;width:534px;height:756px;overflow:hidden}
  .page--cover{left:48px}
  .page--inside{left:625px;top:208px;width:533px;height:754px}
  .photo{position:absolute}
  .photo--cover-bg{inset:0;background:linear-gradient(180deg,#8fb5d8 0%,#dfe8ef 22%,#c9dbe8 45%,#7fb2c9 56%,#4f8fae 66%,#5f7d4a 74%,#495d2c 86%,#2f3a1c 100%)}
  .photo--inside-bg{inset:0;background:linear-gradient(180deg,#2c6f98 0%,#4c93b5 12%,#1f6a9a 30%,#155a87 50%,#17496a 66%,#1f3b2c 80%,#111a12 100%)}
  .photo--inset{left:288px;top:318px;width:189px;height:352px;background:linear-gradient(180deg,#cdd8e0 0%,#9fb9cc 22%,#5f8fae 38%,#4e6750 52%,#3eb7c2 68%,#5c5f56 84%,#3c4a2e 100%)}
  .frame{position:absolute;border:21px solid var(--brand-yellow);border-bottom:none}
  .frame--cover{left:22px;top:20px;width:490px;height:356px}
  .frame--inside{left:22px;top:22px;width:490px;height:648px;border-left:none}
  .frame-leftbar{position:absolute;left:22px;top:22px;width:21px;height:570px;background:var(--brand-yellow)}
  .tagline{position:absolute;top:26px;left:0;width:100%;text-align:center;font:700 7px/10px Roboto,sans-serif;color:var(--brand-blue)}
  .free-inside{position:absolute;right:57px;top:63px;text-align:right;font:500 17px/21px Oswald,sans-serif;color:var(--brand-blue)}
  .free-inside .guide{display:inline-block;background:var(--brand-yellow);padding:0 3px;margin-top:2px}
  .kicker{position:absolute;left:58px;font:500 27px/1 Oswald,sans-serif;color:var(--brand-blue);letter-spacing:-0.5px}
  .kicker--yellow{color:var(--brand-yellow)}
  .title{position:absolute;left:56px;width:421px;height:64px;overflow:visible}
  .title text{font:900 66px Roboto,sans-serif;fill:var(--brand-blue)}
  .title--light text{fill:var(--white)}
  .band{position:absolute;left:56px;width:421px;height:22px;background:var(--brand-yellow)}
  .band text{font:600 17px Oswald,sans-serif;fill:var(--brand-blue)}
  .subtitle{position:absolute;left:0;width:534px;text-align:center;font:400 13px/1 Oswald,sans-serif;color:var(--brand-blue);white-space:nowrap}
  .subtitle--light{color:var(--white)}
  .highlight-box{position:absolute;left:308px;top:376px;width:204px;height:102px;background:var(--brand-yellow);padding:6px 21px 0 0;text-align:right;font:900 27px/31.5px Roboto,sans-serif;color:var(--brand-blue);letter-spacing:-0.5px}
  .status{position:absolute;right:57px;top:485px;text-align:right;font:300 12px/15px Oswald,sans-serif;color:var(--white)}
  .script{position:absolute;left:56px;font:500 26px/32px "Dancing Script",cursive;color:var(--white)}
  .script .first{color:var(--brand-yellow)}
  .body-copy{position:absolute;left:56px;font:400 8px/9.7px Roboto,sans-serif;color:var(--white);text-align:justify;hyphens:auto}
  .body-copy p+p{margin-top:9px}
  .body-copy--inside{font-size:8.3px;line-height:10.8px}
  .body-copy--inside p+p{margin-top:11px}
  .rule{position:absolute;left:56px;top:730px;width:256px;height:1px;background:rgba(255,255,255,.35)}
  .web{position:absolute;font:400 10px/1 Roboto,sans-serif;color:var(--brand-yellow)}
  .partner-mark{position:absolute;left:354px;top:584px;width:128px;height:128px;border-radius:50%;background:var(--white);border:4px solid var(--brand-blue);display:flex;align-items:center;justify-content:center;text-align:center;font:700 13px/16px Roboto,sans-serif;color:var(--brand-blue);padding:14px}
</style>
</head>
<body>
<main class="canvas">

  <section class="page page--cover">
    <div class="photo photo--cover-bg" role="img" aria-label="Hiker with a backpack standing on a grassy headland overlooking a blue lagoon and green island peaks under a cloudy sky"></div>
    <div class="frame frame--cover"></div>
    <p class="tagline">Our globally recognised conservation projects</p>
    <div class="free-inside">FREE INSIDE<br><span class="guide">TRAVELLER GUIDE</span></div>
    <p class="kicker" style="top:129px">A TRAVEL</p>
    <svg class="title" style="top:150px" viewBox="0 0 421 64" aria-label="Conservation"><text x="2" y="60" textLength="417" lengthAdjust="spacingAndGlyphs">CONSERVATION</text></svg>
    <svg class="band" style="top:218px" viewBox="0 0 421 22"><text x="21" y="17" textLength="379" lengthAdjust="spacingAndGlyphs">PROTECTING PARADISE TRAVEL PACKAGES 2019</text></svg>
    <p class="subtitle" style="top:246px">Environmental Adventure &nbsp;|&nbsp; Hiking Citizen Science</p>
    <div class="highlight-box">ONCE IN<br>A LIFETIME<br>EXPERIENCE</div>
    <p class="status">ASSIST IN GLOBALLY RECOGNISED<br>CONSERVATION PROJECTS ON<br>QUILL POINT</p>
    <p class="script" style="top:514px"><span class="first">It was going</span><br>to be a lonely trip back.</p>
    <div class="body-copy" style="top:586px;width:256px">
      <p>Our globally recognised conservation projects have experts from all over the world working side by side with our conservation volunteers, monitoring, collecting and exploring this unique natural environment. Experience nature like nowhere else and be part of sustaining this amazing environment.</p>
      <p>Volunteer as a Citizen Scientist, attend lectures by leading experts, explore the fascinating environment and experience the species that these conservation projects are safeguarding. Your involvement will assist in the species recovery of the world's rarest insect, Quill Point Isle Phasmid, as well as allowing you to participate in a program that will change the lives of critically endangered species including the Quill Point Isle Woodhen; all whilst enjoying the pristine natural environment of Quill Point Isle.</p>
    </div>
    <div class="partner-mark">QPM Habitat Helpers</div>
    <div class="rule"></div>
    <p class="web" style="left:57px;top:735px">www.habitathelpers-trips.com</p>
  </section>

  <section class="page page--inside">
    <div class="photo photo--inside-bg" role="img" aria-label="Aerial view of a turquoise coral reef lagoon with a sandy spit and forested shoreline, fading to dark palm foliage"></div>
    <div class="frame frame--inside"></div>
    <div class="frame-leftbar"></div>
    <p class="tagline" style="top:28px">Our globally recognised conservation projects</p>
    <p class="kicker kicker--yellow" style="top:158px">A TRAVEL</p>
    <svg class="title title--light" style="top:180px" viewBox="0 0 421 64" aria-label="Conservation"><text x="1" y="60" textLength="418" lengthAdjust="spacingAndGlyphs">CONSERVATION</text></svg>
    <svg class="band" style="top:250px" viewBox="0 0 421 22"><text x="21" y="17" textLength="379" lengthAdjust="spacingAndGlyphs">PROTECTING PARADISE TRAVEL PACKAGES 2019</text></svg>
    <p class="subtitle subtitle--light" style="top:281px">Environmental Adventure &nbsp;|&nbsp; Hiking Citizen Science</p>
    <div class="body-copy body-copy--inside" style="left:58px;top:320px;width:220px">
      <p>Lorem Ipsum is simply dummy text of the printing and typesetting industry. Lorem Ipsum has been the industry's standard dummy text ever since the 1500s, when an unknown printer took a galley of type and scrambled it to make a type specimen book. It has survived not only five centuries, but also the leap into electronic typesetting, remaining essentially unchanged. It was popularised in the 1960s with the release of Typeleaf sheets containing Lorem Ipsum passages, and more recently with desktop publishing software like Pagewright Studio including versions of Lorem Ipsum.</p>
      <p>Lorem Ipsum is simply dummy text of the printing and typesetting industry. Lorem Ipsum has been the industry's standard dummy text ever since the 1500s, when an unknown printer took a galley of type and scrambled it to make a type specimen book. It has survived not only five centuries, but also the leap into electronic typesetting, remaining essentially unchanged. It was popularised in the 1960s with the release of Typeleaf sheets containing Lorem Ipsum passages, and more recently with desktop publishing software like Pagewright Studio including versions of Lorem Ipsum.</p>
    </div>
    <div class="photo photo--inset" role="img" aria-label="View down a rocky cliff gully to a turquoise cove with small rocky islets out at sea"></div>
    <p class="script" style="left:58px;top:604px"><span class="first">It was going to</span><br>be a lonely trip back.</p>
    <p class="web" style="left:0;width:533px;text-align:center;top:709px">www.habitathelpers-trips.com</p>
  </section>

</main>
</body>
</html>
```